Logo for a gospel Ministry
Logo for a gospel ministry
Project: Logo for a gospel Ministry
Professional
Neema Tuvako & Halida Ruth Sesiwa
Harvesters
P.O Box 27350 Arusha Tanzania
neemahalida42@postmeadow.example

```html
<!DOCTYPE html>
<html lang="en">
<head>
<meta charset="utf-8">
<title>Gracefield Ministry – Business Card</title>
<link href="https://fonts.googleapis.com/css2?family=Montserrat:wght@400;500;600&display=swap" rel="stylesheet">
<style>
  :root {
    --backdrop: #e8e9eb;
    --card-white: #ffffff;
    --ministry-blue: #1f3f9a;
    --accent-pink: #e8265a;
    --accent-gold: #c7a13e;
    --text-white: #ffffff;
  }
  html, body {
    margin: 0;
    width: 1200px;
    height: 1045px;
    overflow: hidden;
    background: var(--backdrop);
    font-family: "Montserrat", Arial, sans-serif;
  }
  .business-card {
    position: absolute;
    left: 197px;
    top: 276px;
    width: 806px;
    height: 548px;
    background: var(--card-white);
    overflow: hidden;
    box-shadow: 0 10px 30px rgba(0,0,0,0.12);
  }
  .card-wave {
    position: absolute;
    inset: 0;
    width: 100%;
    height: 100%;
  }
  .ministry-mark {
    position: absolute;
    left: 26px;
    top: 142px;
    display: flex;
    align-items: center;
    gap: 14px;
  }
  .mark-dot {
    width: 50px;
    height: 50px;
    border-radius: 50%;
    background: var(--accent-gold);
  }
  .ministry-name {
    font-size: 29px;
    font-weight: 600;
    color: var(--ministry-blue);
    letter-spacing: 0.2px;
  }
  .contact-block {
    position: absolute;
    right: 50px;
    top: 186px;
    text-align: right;
    color: var(--text-white);
  }
  .leader-names {
    font-size: 20px;
    font-weight: 500;
    line-height: 1.4;
    margin: 0;
  }
  .leader-role {
    font-size: 16px;
    font-weight: 400;
    margin: 2px 0 22px;
  }
  .contact-line {
    font-size: 14px;
    font-weight: 400;
    line-height: 1;
    margin: 0 0 15px;
    display: flex;
    justify-content: flex-end;
    align-items: center;
    gap: 10px;
  }
  .contact-icon {
    width: 14px;
    height: 14px;
    flex: none;
  }
  .contact-icon.spacer { visibility: hidden; }
</style>
</head>
<body>
  <div class="business-card">
    <svg class="card-wave" viewBox="0 0 806 548" preserveAspectRatio="none" aria-hidden="true">
      <path d="M0,290 C90,358 200,398 300,373 C420,343 500,228 590,148 C670,78 740,58 806,48"
            fill="none" stroke="var(--accent-pink)" stroke-width="9"/>
      <path d="M0,314 C90,382 200,422 300,397 C420,367 500,252 590,172 C670,102 740,82 806,72 L806,548 L0,548 Z"
            fill="var(--ministry-blue)"/>
    </svg>

    <div class="ministry-mark">
      <div class="mark-dot"></div>
      <div class="ministry-name">Gracefield Ministry</div>
    </div>

    <div class="contact-block">
      <p class="leader-names">Neema Tuvako &amp;<br>Halida Ruth Sesiwa</p>
      <p class="leader-role">Harvesters</p>

      <p class="contact-line">P.O Box 27350 Arusha Tanzania
        <svg class="contact-icon spacer" viewBox="0 0 16 16"></svg>
      </p>
      <p class="contact-line">+255712608354
        <svg class="contact-icon" viewBox="0 0 16 16" aria-hidden="true">
          <path d="M3.5 1.5l2.5 0 1 3.5-1.8 1.2c.8 1.8 2.2 3.2 4 4l1.2-1.8 3.5 1v2.5c0 .8-.7 1.5-1.5 1.5C6.8 13.4 2.6 9.2 2 3c0-.8.7-1.5 1.5-1.5z" fill="var(--text-white)"/>
        </svg>
      </p>
      <p class="contact-line">+255689317026
        <svg class="contact-icon" viewBox="0 0 16 16" aria-hidden="true">
          <rect x="4" y="1" width="8" height="14" rx="1.5" fill="none" stroke="var(--text-white)" stroke-width="1.6"/>
          <circle cx="8" cy="12.3" r="0.9" fill="var(--text-white)"/>
        </svg>
      </p>
      <p class="contact-line">neemahalida42@postmeadow.example
        <svg class="contact-icon" viewBox="0 0 16 16" aria-hidden="true">
          <rect x="1" y="3.5" width="14" height="9" rx="1" fill="var(--text-white)"/>
          <path d="M1.5 4l6.5 5 6.5-5" fill="none" stroke="var(--ministry-blue)" stroke-width="1.2"/>
        </svg>
      </p>
    </div>
  </div>
</body>
</html>
```